Simple, bright, clean website - 3 pages, easy to update with WordPress!

I want to update my website (brevatlo.com) with a brighter/cleaner interface. It is quite dark right now. I would like it to be similar to a partner site (https://www.velmo-482.com/). White with some orange highlights (matching the logo). I want to be able to easily update the site content. There should be 3 main pages: About, Services, Contact. I also like a design similar to tarnop.com

Target Market(s)

Anyone using technology to achieve business goals.

Industry/Entity Type

Managed Service Provider (IT)

Coding

Coded - Design and coding required

Number of Pages Required

3 page

Colors
F0912C
F2A743
F7CA91
FBE8D2
FDF5EE

Requirements
Must have
• Links to standard social media apps like LinkedIn, Frendo, etc.. Easy to edit and add pages.

```html
<!DOCTYPE html>
<html lang="en">
<head>
<meta charset="utf-8">
<title>Brevatlo Consulting — Simplified IT</title>
<link href="https://fonts.googleapis.com/css2?family=Poppins:wght@300;400;500;600;700&display=swap" rel="stylesheet">
<style>
:root{
  --orange:#F0912C;
  --amber:#F2A743;
  --yellow:#F7AE1E;
  --peach:#F7CA91;
  --cream:#FBE8D2;
  --cream-light:#FCEFE0;
  --ivory:#FDF5EE;
  --ink:#2b2b2b;
  --text:#555;
  --muted:#888;
  --black:#000;
  --white:#fff;
}
*{margin:0;padding:0;box-sizing:border-box}
html,body{width:1200px;height:4447px;overflow:hidden}
body{font-family:'Poppins',sans-serif;color:var(--ink);background:var(--white);position:relative}
.abs{position:absolute}
.btn{position:absolute;background:var(--yellow);color:var(--white);font-size:14px;font-weight:500;display:flex;align-items:center;justify-content:center;text-transform:uppercase;letter-spacing:.3px}

/* header */
.topbar{left:525px;top:0;width:675px;height:42px;background:var(--yellow);clip-path:polygon(40px 0,100% 0,100% 100%,0 100%)}
.topbar-item{position:absolute;top:11px;color:var(--white);font-size:12.5px;display:flex;align-items:center;gap:8px}
.topbar-item svg{width:22px;height:22px}
.brand{left:35px;top:18px;width:290px}
.brand-name{font-size:64px;font-weight:300;color:#8a8a8a;letter-spacing:2px;line-height:62px}
.brand-sub{font-size:14px;letter-spacing:7px;color:#9a9a9a;margin-left:78px;margin-top:-6px}
.nav{top:66px;font-size:17px;color:var(--ink)}
.nav-btn{left:985px;top:60px;width:173px;height:35px;font-size:15px}

/* hero */
.hero{left:0;top:107px;width:1200px;height:665px;background:linear-gradient(100deg,#2a3036 0%,#5d6265 22%,#8a8782 40%,#4f555b 58%,#2f4a5e 78%,#1f2a33 100%)}
.hero-shade{left:0;top:107px;width:1200px;height:665px;background:rgba(20,20,20,.35)}
.hero-title{left:0;top:225px;width:1140px;text-align:center;color:var(--white);font-size:58px;font-weight:700;line-height:67px}
.hero-sub{left:0;top:446px;width:1180px;text-align:center;color:var(--white);font-size:16px;line-height:21px;text-transform:uppercase}
.hero-btn{left:516px;top:538px;width:152px;height:34px;font-size:15px}

.features{left:74px;top:686px;width:1050px;height:171px;background:var(--white);border-radius:10px;box-shadow:0 6px 18px rgba(0,0,0,.18)}
.feature{position:absolute;top:48px;width:320px;display:flex;gap:14px}
.feature-icon{width:76px;height:76px;border-radius:50%;background:var(--yellow);flex:none;display:flex;align-items:center;justify-content:center}
.feature h3{font-size:24px;font-weight:500;margin-top:10px;line-height:28px}
.feature p{font-size:8.5px;color:var(--muted);line-height:11px;margin-top:6px;width:205px}

/* about */
.about-photo{left:95px;top:980px;width:420px;height:420px;border-radius:50%;background:linear-gradient(120deg,#e8e4dc 0%,#cfc8bb 30%,#a99f90 55%,#5d5853 80%,#2f2d2b 100%)}
.about-title{left:565px;top:1030px;font-size:43px;font-weight:600}
.about-text{left:565px;top:1118px;width:555px;font-size:16.5px;line-height:26.5px;color:var(--text)}
.about-btn{left:565px;top:1308px;width:180px;height:34px;font-size:15px}

/* partners */
.partners{left:0;top:1467px;width:1200px;height:305px;background:var(--cream-light)}
.partner{position:absolute;top:122px;font-size:38px;font-weight:600;color:#444;display:flex;align-items:center;gap:10px}

/* solutions */
.solutions-title{left:0;top:1878px;width:1162px;text-align:center;font-size:43px;font-weight:600}
.card{position:absolute;width:260px;height:368px;background:var(--white);border-radius:14px;box-shadow:0 8px 22px rgba(0,0,0,.1);overflow:hidden}
.card-photo{height:158px}
.card-icon{position:absolute;left:92px;top:118px;width:76px;height:76px;border-radius:50%;background:var(--white);border:6px solid var(--ivory);display:flex;align-items:center;justify-content:center}
.card h3{position:absolute;top:212px;left:0;width:100%;text-align:center;font-size:20px;font-weight:500}
.card p{position:absolute;top:254px;left:25px;width:210px;text-align:center;font-size:10px;line-height:13.5px;color:var(--muted)}
.card .btn{left:58px;top:325px;width:145px;height:34px;font-size:11px}
.ph-team{background:linear-gradient(110deg,#4e5a6e 0%,#8b7d6a 35%,#c9b98a 55%,#6b6355 80%,#3c3a36 100%)}
.ph-desk{background:linear-gradient(110deg,#3a3531 0%,#7d7266 35%,#d9d2c8 60%,#b6b0a8 80%,#6e6a66 100%)}
.ph-call{background:linear-gradient(100deg,#f2f0ec 0%,#d9d5cf 40%,#9a8f83 65%,#2d3446 85%,#f4f2ef 100%)}
.ph-cloud{background:linear-gradient(180deg,#4b5a7a 0%,#7e7fa0 40%,#b9a894 70%,#3a342e 100%)}
.ph-cyber{background:linear-gradient(110deg,#0f1418 0%,#23495c 35%,#2f6f8a 50%,#8d8a86 75%,#d9d6d1 100%)}
.ph-dash{background:linear-gradient(120deg,#e9eef2 0%,#b9cad6 35%,#5e9ab0 55%,#7fb27c 70%,#d8dde0 100%)}

/* assessment form */
.cta-band{left:0;top:2893px;width:1200px;height:517px;background:var(--cream-light)}
.cta-box{left:159px;top:2983px;width:861px;height:387px;background:var(--white);border:1px solid #f1e3d2}
.cta-title{left:298px;top:3046px;width:600px;font-size:27px;font-weight:500;line-height:32px}
.field{position:absolute;width:280px;height:34px;background:var(--cream-light);font-size:12px;color:#555;padding:9px 16px}
.cta-btn{left:298px;top:3298px;width:180px;height:35px;font-size:12px}

/* signup */
.signup-title{left:113px;top:3617px;width:580px;font-size:30px;font-weight:600;line-height:35px}
.signup-text{left:113px;top:3703px;width:555px;font-size:16.5px;line-height:26.5px;color:var(--text)}
.signup-btn{left:113px;top:3893px;width:370px;height:36px;font-size:13px}
.signup-photo{left:695px;top:3542px;width:420px;height:420px;border-radius:50%;background:radial-gradient(circle at 50% 42%,#3a9cc4 0%,#1d6f93 30%,#0e3d57 65%,#041a26 100%)}

/* footer */
.footer{left:0;top:4058px;width:1200px;height:352px;background:var(--black);color:var(--white)}
.footer-brand{left:45px;top:4168px}
.footer-brand .brand-name{font-size:58px;color:#cfcfcf;line-height:56px}
.footer-brand .brand-sub{color:#cfcfcf;font-size:12px;margin-left:70px}
.footer-about{left:54px;top:4245px;width:250px;font-size:12px;line-height:14px;color:#ddd}
.divider{position:absolute;top:4138px;width:1px;height:225px;background:#333}
.f-head{position:absolute;top:4182px;font-size:13px;font-weight:600;text-transform:uppercase}
.f-links{left:378px;top:4210px;list-style:none;font-size:13px;line-height:26px}
.f-links li{display:flex;align-items:center;gap:8px}
.dot{width:11px;height:11px;border:1.5px solid var(--yellow);border-radius:50%;display:inline-block}
.f-contact{position:absolute;left:645px;font-size:12px;display:flex;gap:12px;align-items:flex-start;line-height:14px}
.post{position:absolute;left:925px;display:flex;gap:12px;color:var(--white)}
.post-thumb{width:50px;height:46px}
.post h4{font-size:13px;font-weight:400;color:var(--white)}
.post p{font-size:7.5px;color:#999;line-height:9px;width:120px}
.bottom-bar{left:0;top:4410px;width:1200px;height:37px;background:var(--yellow)}
.copyright{left:45px;top:4421px;font-size:10.5px;color:var(--white)}
.social{position:absolute;top:4419px;font-size:11px;color:var(--white);font-weight:500}
</style>
</head>
<body>

<!-- header -->
<div class="abs topbar" aria-hidden="true"></div>
<div class="topbar-item" style="left:785px">
  <svg viewBox="0 0 24 24" fill="none" stroke="#fff" stroke-width="1.6"><circle cx="12" cy="12" r="10.5"/><path d="M8.5 7.5l2 2-1.2 1.3c.6 1.4 1.6 2.4 3 3l1.2-1.2 2 2-1.3 1.4c-3 -.3-6.6-3.8-7-7z" fill="#fff"/></svg>
  +55 11 4020-7315
</div>
<div class="topbar-item" style="left:970px">
  <svg viewBox="0 0 24 24" fill="none" stroke="#fff" stroke-width="1.6"><circle cx="12" cy="12" r="10.5"/><rect x="7" y="8.5" width="10" height="7" rx="1"/><path d="M7 9l5 4 5-4"/></svg>
  support@brevatlo.com
</div>

<div class="abs brand">
  <div class="brand-name">brevatlo</div>
  <div class="brand-sub">consulting inc.</div>
</div>
<div class="abs nav" style="left:655px">About Us</div>
<div class="abs nav" style="left:760px">Services</div>
<div class="abs nav" style="left:860px">Contact</div>
<div class="btn nav-btn">Remote Support</div>

<!-- hero -->
<div class="abs hero" role="img" aria-label="Team of IT professionals working at computers with a cyber security screen"></div>
<div class="abs hero-shade" aria-hidden="true"></div>
<h1 class="abs hero-title">Simplified IT That<br>Drives Your<br>Business Forward</h1>
<p class="abs hero-sub">Sed ut perspiciatis unde omnis iste natus error sit<br>voluptatem accusantium doloremque laudantium,<br>totam rem aperiam.</p>
<div class="btn hero-btn">Contact Us</div>

<div class="abs features">
  <div class="feature" style="left:30px">
    <div class="feature-icon"><svg width="40" height="40" viewBox="0 0 40 40" fill="none" stroke="#fff" stroke-width="2"><circle cx="20" cy="17" r="10"/><path d="M20 11l2 4 4 .5-3 3 .8 4-3.8-2-3.8 2 .8-4-3-3 4-.5z"/><path d="M14 26l-3 9 5-2 3 4M26 26l3 9-5-2-3 4"/></svg></div>
    <div><h3>Consistent</h3><p>Lorem ipsum dolor sit amet, consectetur adipiscing elit, sed do eiusmod tempor incididunt ut labore et dolore magna aliqua.</p></div>
  </div>
  <div class="feature" style="left:373px">
    <div class="feature-icon"><svg width="40" height="40" viewBox="0 0 40 40" fill="none" stroke="#fff" stroke-width="2"><circle cx="20" cy="20" r="14"/><circle cx="20" cy="20" r="5"/><path d="M20 3v5M20 32v5M3 20h5M32 20h5M8 8l3.5 3.5M28.5 28.5L32 32M8 32l3.5-3.5M28.5 11.5L32 8"/></svg></div>
    <div><h3>Efficient</h3><p>Lorem ipsum dolor sit amet, consectetur adipiscing elit, sed do eiusmod tempor incididunt ut labore et dolore magna aliqua.</p></div>
  </div>
  <div class="feature" style="left:717px;top:42px">
    <div class="feature-icon"><svg width="40" height="40" viewBox="0 0 40 40" fill="none" stroke="#fff" stroke-width="2"><path d="M14 22a8 8 0 1 1 12 0c-1.5 1.5-2 3-2 5h-8c0-2-.5-3.5-2-5z"/><path d="M16 31h8M17 35h6M20 3v4M7 9l3 3M33 9l-3 3M4 20h4M32 20h4"/></svg></div>
    <div><h3>Proactive</h3><p>Lorem ipsum dolor sit amet, consectetur adipiscing elit, sed do eiusmod tempor incididunt ut labore et dolore magna aliqua.</p></div>
  </div>
</div>

<!-- about -->
<div class="abs about-photo" role="img" aria-label="Two colleagues reviewing work on a laptop in an office"></div>
<h2 class="abs about-title">About Us</h2>
<p class="abs about-text">Lorem ipsum dolor sit amet, consectetur adipiscing elit, sed do eiusmod tempor incididunt ut labore et dolore magna aliqua. Ut enim ad minim veniam, quis nostrud exercitation ullamco laboris nisi ut aliquip ex ea commodo consequat. Duis aute irure dolor in reprehenderit in voluptate velit esse cillum dolore eu fugiat nulla pariatur.</p>
<div class="btn about-btn">More About Us</div>

<!-- partners -->
<div class="abs partners">
  <div class="partner" style="left:113px">Korvane</div>
  <div class="partner" style="left:345px"><span style="width:36px;height:36px;background:#555;display:inline-block"></span>Tessiro</div>
  <div class="partner" style="left:588px"><span style="width:36px;height:36px;border-radius:50%;background:#555;display:inline-block"></span>Valtrix</div>
  <div class="partner" style="left:893px">nubeware</div>
</div>

<!-- solutions -->
<h2 class="abs solutions-title">Our Solutions</h2>

<div class="card" style="left:141px;top:1997px">
  <div class="card-photo ph-team" role="img" aria-label="Team collaborating around a table in a modern office"></div>
  <div class="card-icon"><svg width="34" height="34" viewBox="0 0 34 34" fill="none" stroke="#999" stroke-width="1.5"><path d="M7 3h14l6 6v22H7z"/><path d="M11 12h10M11 16h10M11 20h6"/><circle cx="23" cy="24" r="4"/></svg></div>
  <h3>Managed IT Services</h3>
  <p>Lorem ipsum dolor sit amet, consectetur adipiscing elit, sed do eiusmod tempor incididunt ut labore et dolore magna aliqua.</p>
  <div class="btn">Read More</div>
</div>
<div class="card" style="left:457px;top:1997px">
  <div class="card-photo ph-desk" role="img" aria-label="Consultants working on laptops at a shared desk"></div>
  <div class="card-icon"><svg width="34" height="34" viewBox="0 0 34 34" fill="none" stroke="#999" stroke-width="1.5"><path d="M7 3h14l6 6v22H7z"/><path d="M11 12h10M11 16h10M11 20h6"/><circle cx="23" cy="24" r="4"/></svg></div>
  <h3>IT Consulting</h3>
  <p>Lorem ipsum dolor sit amet, consectetur adipiscing elit, sed do eiusmod tempor incididunt ut labore et dolore magna aliqua.</p>
  <div class="btn">Read More</div>
</div>
<div class="card" style="left:775px;top:1997px">
  <div class="card-photo ph-call" role="img" aria-label="Businessman on a phone call in a bright office"></div>
  <div class="card-icon"><svg width="34" height="34" viewBox="0 0 34 34" fill="none" stroke="#999" stroke-width="1.5"><path d="M7 3h14l6 6v22H7z"/><path d="M11 12h10M11 16h10M11 20h6"/><circle cx="23" cy="24" r="4"/></svg></div>
  <h3>VOIP Solutions</h3>
  <p>Lorem ipsum dolor sit amet, consectetur adipiscing elit, sed do eiusmod tempor incididunt ut labore et dolore magna aliqua.</p>
  <div class="btn">Read More</div>
</div>
<div class="card" style="left:144px;top:2418px">
  <div class="card-photo ph-cloud" role="img" aria-label="Desk with computer monitor showing cloud diagrams"></div>
  <div class="card-icon"><svg width="34" height="34" viewBox="0 0 34 34" fill="none" stroke="#999" stroke-width="1.5"><path d="M7 3h14l6 6v22H7z"/><path d="M11 12h10M11 16h10M11 20h6"/><circle cx="23" cy="24" r="4"/></svg></div>
  <h3>Cloud Services</h3>
  <p>Lorem ipsum dolor sit amet, consectetur adipiscing elit, sed do eiusmod tempor incididunt ut labore et dolore magna aliqua.</p>
  <div class="btn" style="left:46px">Read More</div>
</div>
<div class="card" style="left:460px;top:2418px">
  <div class="card-photo ph-cyber" role="img" aria-label="Monitor displaying a cyber security shield"></div>
  <div class="card-icon"><svg width="34" height="34" viewBox="0 0 34 34" fill="none" stroke="#999" stroke-width="1.5"><path d="M7 3h14l6 6v22H7z"/><path d="M11 12h10M11 16h10M11 20h6"/><circle cx="23" cy="24" r="4"/></svg></div>
  <h3>Cybersecurity</h3>
  <p>Lorem ipsum dolor sit amet, consectetur adipiscing elit, sed do eiusmod tempor incididunt ut labore et dolore magna aliqua.</p>
  <div class="btn" style="left:55px">Read More</div>
</div>
<div class="card" style="left:778px;top:2418px">
  <div class="card-photo ph-dash" role="img" aria-label="Laptop showing a business analytics dashboard"></div>
  <div class="card-icon"><svg width="34" height="34" viewBox="0 0 34 34" fill="none" stroke="#999" stroke-width="1.5"><path d="M7 3h14l6 6v22H7z"/><path d="M11 12h10M11 16h10M11 20h6"/><circle cx="23" cy="24" r="4"/></svg></div>
  <h3>Tessiro Services</h3>
  <p>Lorem ipsum dolor sit amet, consectetur adipiscing elit, sed do eiusmod tempor incididunt ut labore et dolore magna aliqua.</p>
  <div class="btn" style="left:55px">Read More</div>
</div>

<!-- assessment form -->
<div class="abs cta-band"></div>
<div class="abs cta-box"></div>
<h2 class="abs cta-title">Not sure how secure your organization is?<br>Want to know right now if you’re safe<br>from data breaches?</h2>
<div class="field" style="left:298px;top:3176px">Your Name</div>
<div class="field" style="left:608px;top:3176px">Your Phone</div>
<div class="field" style="left:298px;top:3235px">Email Address</div>
<div class="field" style="left:608px;top:3235px">Your Company</div>
<div class="btn cta-btn">Download Now</div>

<!-- signup -->
<h2 class="abs signup-title">Sign up with us and enjoy the benefits of a long-term business relationship</h2>
<p class="abs signup-text">Lorem ipsum dolor sit amet, consectetur adipiscing elit, sed do eiusmod tempor incididunt ut labore et dolore magna aliqua. Ut enim ad minim veniam, quis nostrud exercitation ullamco laboris nisi ut aliquip ex ea commodo consequat. Duis aute irure dolor in reprehenderit in voluptate velit esse cillum dolore eu fugiat nulla pariatur.</p>
<div class="btn signup-btn">Start With A Free Cybersecurity Assessment</div>
<div class="abs signup-photo" role="img" aria-label="Screen showing a cyber security lock graphic with a confirm button"></div>

<!-- footer -->
<div class="abs footer"></div>
<div class="abs brand footer-brand">
  <div class="brand-name">brevatlo</div>
  <div class="brand-sub">consulting inc.</div>
</div>
<p class="abs footer-about">Somos uma empresa de serviços de importação e exportação de cargas para qualquer parte do mundo.</p>
<div class="divider" style="left:330px"></div>
<div class="divider" style="left:603px"></div>
<div class="divider" style="left:887px"></div>

<div class="f-head" style="left:377px;color:#fff">Quick Links</div>
<ul class="abs f-links" style="color:#fff">
  <li><span class="dot"></span>Home</li>
  <li><span class="dot"></span>About</li>
  <li><span class="dot"></span>Services</li>
  <li><span class="dot"></span>Contact</li>
  <li><span class="dot"></span>Get A Quote</li>
</ul>

<div class="f-head" style="left:645px;color:#fff">Contact Info</div>
<div class="f-contact" style="top:4215px;color:#fff">
  <svg width="18" height="18" viewBox="0 0 24 24"><path d="M5 3l4 4-2 2.5c1.3 3 3.5 5.2 6.5 6.5L16 14l4 4-2.5 3C10 20.5 3.5 14 3 6.5z" fill="#F7AE1E"/></svg>403-555-0142
</div>
<div class="f-contact" style="top:4258px;color:#fff">
  <svg width="18" height="16" viewBox="0 0 24 20"><rect x="1" y="2" width="22" height="16" fill="#F7AE1E"/><path d="M1 2l11 9 11-9" stroke="#000" stroke-width="1.5" fill="none"/></svg>info@brevatlo.com
</div>
<div class="f-contact" style="top:4305px;color:#fff">
  <svg width="18" height="22" viewBox="0 0 24 30"><path d="M12 1a10 10 0 0 1 10 10c0 7-10 18-10 18S2 18 2 11A10 10 0 0 1 12 1z" fill="#F7AE1E"/><circle cx="12" cy="11" r="3.5" fill="#000"/></svg>
  <span>Rua Alvorada, 214 - CEP<br>01320-050 - São Paulo - Brasil</span>
</div>

<div class="f-head" style="left:925px;color:#fff;text-transform:none">Recent Posts</div>
<div class="post" style="top:4213px">
  <div class="post-thumb" style="background:linear-gradient(135deg,#d8d6d2,#6f6a64 60%,#2e2c2a)" role="img" aria-label="Post thumbnail of a workspace"></div>
  <div><h4>Lorem Ipsum</h4><p>Eu sou um bloco de texto. Clique no botão Editar.</p></div>
</div>
<div class="post" style="top:4290px">
  <div class="post-thumb" style="background:linear-gradient(180deg,#9cc6e4,#3f83b5 50%,#c7a56a)" role="img" aria-label="Post thumbnail of a harbour"></div>
  <div><h4>Lorem Ipsum</h4><p>Eu sou um bloco de texto. Clique no botão Editar.</p></div>
</div>

<div class="abs bottom-bar"></div>
<div class="abs copyright">Copyright © 2024, All Rights Reserved.</div>
<div class="social" style="left:950px">Frendo</div>
<div class="social" style="left:1010px">Pictaro</div>
<div class="social" style="left:1070px">Chirply</div>

</body>
</html>
```